BHSM Business Card Design Project

We are a Wedding Film company in Charleston, SC In need of a unique business card. Our website is www.brightharborstudiomedia.com. Check us out to get an idea of who we are and what we do. The design should be upscale but not pretentious. Modern but not cheesy. I will most likely have our cards printed by Zell on the Plume design. I'm also liking the raised designs for our logo. The Wedding Films in our logo on our site is blue so feel free to manipulate our logo for your designs as well.

Industry/Entity Type

Business

Requirements
Must have
• This is the info I want on the card:

Derek Halloway
Storyteller

Brightharbor Studio Media
www.brightharborstudiomedia.com

843.627.4150
derek@brightharborstudiomedia.com

```html
<!DOCTYPE html>
<html lang="en">
<head>
<meta charset="utf-8">
<title>Brightharbor Studio Media – Business Card</title>
<link rel="stylesheet" href="https://fonts.googleapis.com/css2?family=Arimo:wght@400;700&display=swap">
<style>
  :root {
    --backdrop: #d9d6d0;
    --card-dark: #1b1e21;
    --card-mid: #2b3034;
    --card-light: #4a5258;
    --gold: #dcc479;
    --gold-soft: #e9d996;
    --ink-light: #ece7d6;
  }
  * { box-sizing: border-box; margin: 0; padding: 0; }
  html, body {
    width: 1200px;
    height: 534px;
    overflow: hidden;
    background: var(--backdrop);
    font-family: "Arimo", Arial, sans-serif;
  }
  .canvas {
    position: relative;
    width: 1200px;
    height: 534px;
  }
  .card {
    position: absolute;
    top: 118px;
    width: 517px;
    height: 295px;
    background:
      linear-gradient(172deg, rgba(255,255,255,0) 30%, rgba(255,255,255,0.05) 55%, rgba(255,255,255,0) 75%),
      linear-gradient(160deg, var(--card-dark) 0%, var(--card-mid) 55%, var(--card-light) 100%);
    box-shadow: 0 2px 6px rgba(0,0,0,0.25);
    overflow: hidden;
  }
  .card--front { left: 62px; }
  .card--back { left: 620px; }

  /* Front */
  .front-mark {
    position: absolute;
    left: 0;
    right: 0;
    top: 130px;
    text-align: center;
    color: var(--gold);
    font-weight: 400;
    font-size: 34px;
    letter-spacing: 1px;
  }

  /* Back */
  .back-mark {
    position: absolute;
    left: 51px;
    top: 86px;
    color: var(--gold);
    font-weight: 400;
    font-size: 15px;
    letter-spacing: 0.5px;
  }
  .contact {
    position: absolute;
    left: 51px;
    top: 144px;
    color: var(--ink-light);
  }
  .contact__name {
    color: var(--gold-soft);
    font-weight: 700;
    font-size: 19px;
    letter-spacing: 0.5px;
  }
  .contact__role {
    color: var(--ink-light);
    font-weight: 700;
    font-size: 11.5px;
    margin-top: 2px;
  }
  .contact__company {
    color: var(--gold-soft);
    font-weight: 700;
    font-size: 12.5px;
    margin-top: 18px;
  }
  .contact__lines {
    list-style: none;
    font-size: 12.5px;
    line-height: 15.5px;
    margin-top: 3px;
  }
  .contact__label { display: inline-block; width: 20px; }
</style>
</head>
<body>
  <main class="canvas">
    <section class="card card--front" aria-label="Card front">
      <div class="front-mark">Brightharbor Studio Media</div>
    </section>

    <section class="card card--back" aria-label="Card back">
      <div class="back-mark">Brightharbor Studio Media</div>
      <div class="contact">
        <p class="contact__name">Derek Halloway</p>
        <p class="contact__role">Storyteller</p>
        <p class="contact__company">Brightharbor Studio Media</p>
        <ul class="contact__lines">
          <li><span class="contact__label">p :</span>+ 843.627.4150</li>
          <li><span class="contact__label">e :</span>derek@brightharborstudiomedia.com</li>
          <li><span class="contact__label">w :</span>www.brightharborstudiomedia.com</li>
        </ul>
      </div>
    </section>
  </main>
</body>
</html>
```